UPDATED Drawing Nearer: A Memoir after Divorce

I need a cover front, spine and back, for e book and print for a memoir that is for women, and perhaps some men. It is modern, about the modern world, and yet must indicate how we strive for intimacy in a modern tech age. There are laugh out loud moments, and poignant moments. It is upbeat, thoughtful, and full of characters.

We have two images in mind.

The first involves showing a woman's dress with angel wings on it, or a high heeled shoe with angel wings on it, or perhaps a pair of women's earrings with angel wings. It must indicate a woman who is modern going dating again (ie a dress), but who is thinking now about her spirituality (ie angel wings). There are lots of images out there and I have attached a few for reference. Soft colours here: feminine luxury read.

The other image I first had in mind is a friendly font, something like was used for the UK edition of Tide Under Glass by Penny Varlow, against white, with a small image of two brixo-type yellow figures, one male, one female, under a bed sheet. Or the early human computer figures of the 1980s, in a funny position suggesting a goal for relationship but the distance of computer created identikit people. You know those people they made of little yellow pixelated squares? :)

Title is Drawing Nearer

Subtitle, smaller, A Memoir after Divorce

Author name is Marla Quinby

Press is Halvern Press and the logo for the spine is attached.

Thank you! Have fun :)

Target Market(s)

UK and US women (perhaps Europe) from 28-34 with some range either way. Not to exclude men. Think Walk Sing Rest audience, and W is for Wren audience. Both those covers might be useful. Also think of the book The Pursuit. Memoirs that have hit the bestseller lists with an honest take on love, sex, dating and Drawing Nearer. We are not looking to sexy with the small image: humorous and of a period, hence the idea for munchbot style people or brixo people under the sheets.

Font styles to use
Other font styles liked:
• modern design fonts, art house fonts

Requirements
Must have
• Warmth, sophistication, humour. It's a book for readers. A simple, clear marketing on the front with the font, colour and image. Modern, not to fresh but not romantic and feminine. Think city woman on a retreat to touch the heart.
Nice to have
• A smile on looking at it. Fonts that are not too square. Some fluidity in the font to show some emotional flow. Not too stark. See other covers on my site marlaquinby.example. (Mostly Studio Flock). This should look different again but fit the brand.

```html
<!DOCTYPE html>
<html lang="en">
<head>
<meta charset="utf-8">
<title>Drawing Nearer: A Memoir after Divorce – Marla Quinby</title>
<link rel="stylesheet" href="https://fonts.googleapis.com/css2?family=Amatic+SC:wght@700&family=Caveat:wght@500&family=Cormorant+Garamond:wght@500&display=swap">
<style>
  :root {
    --backdrop: #979493;
    --paper: #ffffff;
    --title-red: #e20e1c;
    --ink: #1a1a1a;
    --wing-light: #e9e9e9;
    --shoe-dark: #1c1c1c;
  }
  html, body {
    margin: 0;
    padding: 0;
    width: 1200px;
    height: 823px;
    overflow: hidden;
    background: var(--backdrop);
  }
  .stage {
    position: relative;
    width: 1200px;
    height: 823px;
  }
  .book-cover {
    position: absolute;
    left: 350px;
    top: 23px;
    width: 500px;
    height: 776px;
    background: var(--paper);
  }
  .book-cover svg {
    display: block;
    width: 500px;
    height: 776px;
  }
  .title-line {
    font-family: "Amatic SC", "Caveat", cursive;
    font-weight: 700;
    fill: var(--title-red);
  }
  .subtitle {
    font-family: "Caveat", cursive;
    font-weight: 500;
    font-size: 36px;
    fill: var(--title-red);
  }
  .author {
    font-family: "Cormorant Garamond", Georgia, serif;
    font-weight: 500;
    font-size: 31px;
    letter-spacing: 3px;
    fill: var(--ink);
  }
  .publisher {
    font-family: "Cormorant Garamond", Georgia, serif;
    font-weight: 500;
    font-size: 14px;
    letter-spacing: 1.5px;
    fill: var(--ink);
  }
</style>
</head>
<body>
<main class="stage">
  <section class="book-cover" aria-label="Front cover of Drawing Nearer: A Memoir after Divorce by Marla Quinby">
    <svg viewBox="0 0 500 776" xmlns="http://www.w3.org/2000/svg">
      <defs>
        <linearGradient id="winged-shoe-tone" x1="0" y1="0" x2="0" y2="1">
          <stop offset="0" stop-color="var(--wing-light)"/>
          <stop offset="0.45" stop-color="#8a8a8a"/>
          <stop offset="1" stop-color="var(--shoe-dark)"/>
        </linearGradient>
      </defs>

      <rect class="cover-illustration" x="176" y="7" width="313" height="262" rx="24"
            fill="url(#winged-shoe-tone)" role="img"
            aria-label="Illustration of a black high-heeled shoe with a red sole and white angel wings"/>

      <text class="title-line" x="63" y="390" font-size="190"
            textLength="378" lengthAdjust="spacingAndGlyphs">DRAWING</text>
      <text class="title-line" x="71" y="494" font-size="140"
            textLength="330" lengthAdjust="spacingAndGlyphs">NEARER:</text>

      <text class="subtitle" x="73" y="549"
            textLength="359" lengthAdjust="spacingAndGlyphs">A Memoir after Divorce</text>

      <text class="author" x="250" y="641" text-anchor="middle">MARLA QUINBY</text>

      <g class="publisher-mark">
        <circle cx="250" cy="712" r="6" fill="var(--ink)"/>
        <text class="publisher" x="250" y="740" text-anchor="middle">HALVERN PRESS</text>
      </g>
    </svg>
  </section>
</main>
</body>
</html>
```